Exclusive Pet groomer Post Card

We need a design for a direct mailing postcard. We want to include images of some of dogs and cats done the list of our services and the benefits of our company.

I like something like: Does your pet look like any of these or is a similar breed?

If your answer is yes, then it deserves the best groomer in town

any ideas are welcome!
Updates

URGENT Mailing Postcard needed!

Elegant, modern and clean sophisticated card that has images of the dogs and cats provided. I will use the original images from the image bank once the project is approved. As a designer you just need to create the layout for this and the organization!

Thanks

Target Market(s)

High Income professionals that will pay for premium services for their pets.

Industry/Entity Type

Pet

Requirements
Must have
• A full color double sided postcard. 5.5 x 8.5 in postcard. (I want to have all pics uploaded. I used some sample images from stock photo but once approved I will purchase the images at the respective site). Must have space to place recipient address and space for NPDS stamp. ( is a postcard to be mailed!)

I would like to have the following text in the post card:

Enhance the beauty of your pets
Pamper your best friend
Give to your dog or cat the stylish treatment it deserves

One of the top groomers in town
Experienced in dogs and cats
Clean individual pet grooming stations (Sanitation and Sterilization)
Services:
Full service grooming* services for dogs and cats include:
Day Spa, High Fashion Haircuts, hair trimming, nail clipping and “Petticures”
Bathing, gentle ear Cleaning, sanitary trim, Brushing, Fluff Drying and Dematting
* Regular grooming ensures happier and healthier pets

Fur Harbor Trim
2671 SW 87th Avenue, Coral Bend, Florida 33029
T. 305-417-6382
www.furharbortrim.example
Nice to have
• Logo as in the website

```html
<!DOCTYPE html>
<html lang="en">
<head>
<meta charset="utf-8">
<title>Fur Harbor Trim – Mailing Postcard</title>
<link rel="stylesheet" href="https://fonts.googleapis.com/css2?family=Montserrat:ital,wght@0,700;0,800;1,700&family=Arimo:wght@400;700&display=swap">
<style>
  :root {
    --stage: #3d3d3d;
    --card: #ffffff;
    --purple: #4e1d87;
    --magenta: #c03fc6;
    --ink: #222222;
    --rule: #9a9a9a;
    --fur-light: #e9c9a0;
    --fur-dark: #7a4a22;
    --cat-light: #f3e3cc;
    --cat-mid: #d9a56b;
    --stamp: #8a5fa6;
  }
  * { margin: 0; padding: 0; box-sizing: border-box; }
  html, body { width: 1200px; height: 596px; overflow: hidden; }
  body { background: var(--stage); position: relative; font-family: "Arimo", Arial, sans-serif; color: var(--ink); }

  .postcard { position: absolute; top: 53px; width: 531px; height: 342px; background: var(--card); overflow: hidden; }
  .postcard--front { left: 42px; }
  .postcard--back { left: 627px; }
  .postcard__art { position: absolute; inset: 0; width: 100%; height: 100%; }

  .headline { position: absolute; color: #fff; font-family: "Montserrat", Arial, sans-serif; font-weight: 800; text-shadow: 1px 2px 3px rgba(0,0,0,.45); }
  .headline--front { left: 16px; top: 46px; font-size: 21.5px; line-height: 26px; transform: rotate(-6deg); transform-origin: 0 0; white-space: nowrap; }
  .headline--back { left: 22px; top: 14px; font-size: 15px; line-height: 18.5px; font-weight: 700; }

  .benefits { position: absolute; left: 0; top: 210px; width: 282px; text-align: center; color: var(--magenta); font-family: "Montserrat", Arial, sans-serif; font-style: italic; font-weight: 700; font-size: 11.6px; line-height: 13.4px; }

  .brand { position: absolute; width: 108px; display: flex; flex-direction: column; align-items: center; }
  .brand__dot { width: 16px; height: 16px; border-radius: 50%; background: var(--purple); margin-bottom: 8px; }
  .brand__name { font-family: "Montserrat", Arial, sans-serif; font-weight: 700; color: var(--purple); font-size: 10px; line-height: 12px; white-space: nowrap; }
  .postcard--front .brand { left: 10px; top: 286px; }
  .postcard--back .brand { left: 12px; top: 282px; }

  .contact { position: absolute; padding-left: 8px; border-left: 1px solid var(--rule); font-size: 9.5px; line-height: 11.5px; font-style: normal; }
  .postcard--front .contact { left: 123px; top: 287px; }
  .postcard--back .contact { left: 125px; top: 282px; }
  .contact__phone { color: var(--magenta); font-family: "Montserrat", Arial, sans-serif; font-weight: 700; font-size: 14px; line-height: 17px; }

  .services { position: absolute; left: 22px; top: 206px; width: 262px; font-size: 6.8px; line-height: 9.6px; white-space: nowrap; }
  .services__title { font-size: 10.5px; line-height: 12px; }

  .address-lines { position: absolute; left: 291px; top: 185px; width: 201px; }
  .address-lines span { display: block; height: 1px; background: var(--rule); margin-bottom: 23px; }
</style>
</head>
<body>

<section class="postcard postcard--front" aria-label="Postcard front">
  <svg class="postcard__art" viewBox="0 0 531 342" preserveAspectRatio="none">
    <defs>
      <radialGradient id="dogTones" cx="0.55" cy="0.6" r="0.6">
        <stop offset="0" stop-color="#7a4a22"/>
        <stop offset="0.55" stop-color="#e9c9a0"/>
        <stop offset="1" stop-color="#ffffff"/>
      </radialGradient>
    </defs>
    <rect x="280" y="60" width="251" height="282" fill="url(#dogTones)" role="img" aria-label="Photo of a groomed Yorkshire terrier with a pink bow lying down"/>
    <path d="M0 0 H531 V80 C430 106 330 186 250 198 C180 208 80 196 0 190 Z" fill="var(--magenta)"/>
    <path d="M0 0 H531 V72 C430 98 320 178 250 190 C180 200 80 188 0 182 Z" fill="var(--purple)"/>
  </svg>

  <h1 class="headline headline--front">Enhance the beauty of your pets<br>Pamper your best friend<br>Give to your dog or cat the stylish<br>treatment it deserves</h1>

  <p class="benefits">One of the top groomers in town,<br>Experienced in dogs and cats<br>Clean individual pet grooming stations<br>(Sanitation and Sterilization)</p>

  <div class="brand"><span class="brand__dot"></span><span class="brand__name">FUR HARBOR TRIM</span></div>
  <address class="contact">
    2671 SW 87th Avenue,<br>Coral Bend, Florida 33029
    <div class="contact__phone">Call 305-417-6382</div>
    www.furharbortrim.example
  </address>
</section>

<section class="postcard postcard--back" aria-label="Postcard back">
  <svg class="postcard__art" viewBox="0 0 531 342" preserveAspectRatio="none">
    <defs>
      <radialGradient id="catTones" cx="0.5" cy="0.55" r="0.55">
        <stop offset="0" stop-color="#d9a56b"/>
        <stop offset="0.6" stop-color="#f3e3cc"/>
        <stop offset="1" stop-color="#ffffff"/>
      </radialGradient>
    </defs>
    <path d="M0 0 H382 C340 44 285 96 205 117 C140 128 60 125 0 123 Z" fill="var(--magenta)"/>
    <path d="M0 0 H370 C330 40 280 90 200 110 C140 122 60 118 0 116 Z" fill="var(--purple)"/>
    <rect x="22" y="108" width="205" height="96" fill="url(#catTones)" role="img" aria-label="Photo of a fluffy Persian cat"/>
    <rect x="365" y="12" width="135" height="85" fill="#f4f2f4"/>
    <g fill="none" stroke="#8a8a8a" stroke-width="1.2">
      <path d="M378 32 q10 -6 20 0 t20 0 t20 0 t20 0"/>
      <path d="M378 44 q10 -6 20 0 t20 0 t20 0 t20 0"/>
      <path d="M378 56 q10 -6 20 0 t20 0 t20 0 t20 0"/>
      <path d="M378 68 q10 -6 20 0 t20 0 t20 0 t20 0"/>
    </g>
    <rect x="446" y="20" width="44" height="60" fill="var(--stamp)" role="img" aria-label="Postage stamp for NPDS mailing"/>
  </svg>

  <h2 class="headline headline--back">Enhance the beauty of your pets<br>Pamper your best friend<br>Give to your dog or cat the<br>stylish treatment it deserves</h2>

  <div class="services">
    <p class="services__title">Services:</p>
    <p>Full service grooming* services for dogs and cats include:<br>
    Day Spa, High Fashion Haircuts, hair trimming, nail clipping and “Petticures”<br>
    Bathing, gentle ear Cleaning, sanitary trim, Brushing, Fluff Drying and Dematting<br>
    * Regular grooming ensures happier and healthier pets</p>
  </div>

  <div class="brand"><span class="brand__dot"></span><span class="brand__name">FUR HARBOR TRIM</span></div>
  <address class="contact">
    2671 SW 87th Avenue,<br>Coral Bend, Florida 33029
    <div class="contact__phone">Call 305-417-6382</div>
    www.furharbortrim.example
  </address>

  <div class="address-lines" aria-label="Recipient address"><span></span><span></span><span></span><span></span><span></span></div>
</section>

</body>
</html>
```